Website and business logo needed

Organisation for the community providing dispute resolution services, peace building.

I'd like calm colours, a strong simple logo symbolising collaboration, peace and cohesion. Needs to convey that message in a symbol.

We provide different types of services so we do mediation, and training and provide publications and research. It's community based and designed to work with the community for the community.

Industry/Entity Type

Training

Contact Information for Business Card

Quiet Harbour - Institute for Neighbourhood and Conflict Settlement
communication skills, mediation, facilitation, conflict coaching, education, training, research
PO Box 7416
South Brisbane
0418 627 903

Requirements
Must have
• Logo
Calm but strong colours

```html
<!DOCTYPE html>
<html lang="en">
<head>
<meta charset="utf-8">
<title>Quiet Harbour – Business Card</title>
<link rel="stylesheet" href="https://fonts.googleapis.com/css2?family=Montserrat:wght@700&family=Ubuntu:wght@400&display=swap">
<style>
  :root {
    --stage: #2a2a2c;
    --card-dark: #3d3e40;
    --card-light: #f3f4f6;
    --brand-blue: #1b93d8;
    --text-grey: #8a8c90;
    --faint-blue: #dbe6ee;
    --faint-grey: #e6e7e9;
  }
  * { box-sizing: border-box; margin: 0; padding: 0; }
  html, body {
    width: 1200px; height: 900px; overflow: hidden;
    background: var(--stage);
  }
  .stage {
    position: relative; width: 1200px; height: 900px;
    display: flex; flex-direction: column; align-items: center; justify-content: center;
    gap: 56px;
  }
  .card {
    position: relative; width: 600px; height: 343px; overflow: hidden;
    box-shadow: 0 14px 30px rgba(0,0,0,.45);
  }
  .card--back { background: var(--card-dark); display: flex; align-items: center; justify-content: center; gap: 18px; }
  .card--front { background: var(--card-light); }

  .brand-mark {
    display: inline-block; border-radius: 50%; background: var(--brand-blue); flex: none;
  }
  .brand-name {
    font-family: "Montserrat", sans-serif; font-weight: 700;
    color: var(--brand-blue); letter-spacing: -0.5px; white-space: nowrap;
  }
  .card--back .brand-mark { width: 58px; height: 58px; }
  .card--back .brand-name { font-size: 44px; }

  .backdrop-circle {
    position: absolute; right: -70px; top: -40px; width: 330px; height: 330px;
    border-radius: 50%; border: 46px solid var(--faint-blue); opacity: .75;
  }
  .front-content { position: absolute; left: 44px; top: 92px; right: 40px; }
  .front-brand { display: flex; align-items: center; gap: 14px; }
  .front-brand .brand-mark { width: 40px; height: 40px; }
  .front-brand .brand-name { font-size: 29px; }
  .services {
    margin-top: 22px; max-width: 440px;
    font-family: "Ubuntu", sans-serif; font-size: 12.5px; line-height: 1.3; color: var(--text-grey);
  }
  .contact { margin-top: 30px; list-style: none; font-family: "Ubuntu", sans-serif; font-size: 18px; color: var(--text-grey); }
  .contact li { display: flex; align-items: center; gap: 8px; margin-bottom: 6px; }
  .contact svg { width: 15px; height: 17px; fill: var(--brand-blue); flex: none; }
</style>
</head>
<body>
<main class="stage">
  <section class="card card--back" aria-label="Card back">
    <span class="brand-mark"></span>
    <span class="brand-name">Quiet Harbour</span>
  </section>

  <section class="card card--front" aria-label="Card front">
    <div class="backdrop-circle" aria-hidden="true"></div>
    <div class="front-content">
      <div class="front-brand">
        <span class="brand-mark"></span>
        <span class="brand-name">Quiet Harbour</span>
      </div>
      <p class="services">Institute for Neighbourhood and Conflict Settlement communication skills, mediation, facilitation, conflict coaching, education, training, research</p>
      <ul class="contact">
        <li>
          <svg viewBox="0 0 16 20" aria-hidden="true"><path d="M8 0a7 7 0 0 0-7 7c0 5 7 13 7 13s7-8 7-13a7 7 0 0 0-7-7zm0 10a3 3 0 1 1 0-6 3 3 0 0 1 0 6z"/></svg>
          <span>PO Box 7416 South Brisbane</span>
        </li>
        <li>
          <svg viewBox="0 0 16 18" aria-hidden="true"><path d="M2 1h3v16H2a1 1 0 0 1-1-1V2a1 1 0 0 1 1-1zm4 2h8a1 1 0 0 1 1 1v12a1 1 0 0 1-1 1H6zm2 2v3h5V5zm0 5v2h2v-2zm3 0v2h2v-2zm-3 3v2h2v-2zm3 0v2h2v-2z"/></svg>
          <span>0418 627 903</span>
        </li>
      </ul>
    </div>
  </section>
</main>
</body>
</html>
```